Property Management Company Business Cards

Need business cards for a property management company located in Michigan. We manage houses for clients all over the world. Young and modern company, looking for eye catching design. Please work with the attached logo.

Industry/Entity Type

Property Management

Requirements
Must have
• Need lines for address, telephone number, fax number, web site.

Also lines for name, and job title

```html
<!DOCTYPE html>
<html lang="en">
<head>
<meta charset="utf-8">
<title>Harbor Point Management – Business Cards</title>
<link href="https://fonts.googleapis.com/css2?family=Open+Sans:wght@400;600;700&display=swap" rel="stylesheet">
<style>
  :root {
    --stage: #000000;
    --frame: #ffffff;
    --card-light: #ffffff;
    --card-shade: #ececec;
    --ink: #3c3c3c;
    --ink-soft: #4a4a4a;
    --brand-blue: #3a9fd8;
  }
  * { box-sizing: border-box; margin: 0; padding: 0; }
  html, body {
    width: 1043px; height: 1200px; overflow: hidden;
    background: var(--stage);
    font-family: "Open Sans", Arial, sans-serif;
  }
  .presentation { position: relative; width: 1043px; height: 1200px; background: var(--stage); }
  .frame {
    position: absolute; left: 41px; top: 41px; width: 961px; height: 1117px;
    border: 24px solid var(--frame);
  }
  .card {
    position: absolute;
    background: linear-gradient(135deg, var(--card-light) 0%, var(--card-light) 45%, var(--card-shade) 100%);
    overflow: hidden;
  }
  .card--front { left: 132px; top: 117px; width: 770px; height: 440px; }
  .card--back { left: 136px; top: 622px; width: 768px; height: 437px; }

  .front__topline { position: absolute; left: 0; top: 2px; width: 100%; height: 3px; background: var(--brand-blue); }

  .brand { position: absolute; left: 14px; top: 45px; display: flex; align-items: center; gap: 24px; }
  .brand__dot { width: 122px; height: 122px; border-radius: 50%; background: var(--brand-blue); flex: none; }
  .brand__name { color: var(--ink); font-weight: 700; line-height: 1; }
  .brand__line1 { display: block; font-size: 66px; letter-spacing: -0.5px; }
  .brand__line2 { display: block; font-size: 27px; letter-spacing: 35px; margin-top: 10px; }

  .person { position: absolute; right: 16px; top: 222px; text-align: right; }
  .person__name { font-size: 33px; font-weight: 400; color: var(--ink); line-height: 1.2; }
  .person__title { font-size: 18px; color: var(--brand-blue); line-height: 1.15; margin-top: 2px; }
  .person__cell { font-size: 18px; color: var(--ink); line-height: 1.15; }

  .contact { position: absolute; left: 66px; top: 264px; font-size: 18.5px; color: var(--ink-soft); line-height: 27px; font-style: normal; }
  .contact__row { display: flex; align-items: center; gap: 6px; }
  .contact__row--indent { padding-left: 3px; }
  .contact__icon { width: 22px; height: 16px; flex: none; }
  .contact__gap { width: 14px; }

  .front__bands { position: absolute; left: 0; top: 398px; width: 770px; height: 42px; }
  .front__web {
    position: absolute; right: 28px; top: 406px; font-size: 19px; color: var(--ink); line-height: 26px;
  }

  .back__brand { position: absolute; left: 0; top: 52px; width: 100%; display: flex; flex-direction: column; align-items: center; }
  .back__dot { width: 150px; height: 150px; border-radius: 50%; background: var(--brand-blue); }
  .back__name { margin-top: 34px; font-size: 46px; font-weight: 700; color: var(--ink); line-height: 1.15; text-align: center; }
  .back__web { position: absolute; left: 0; width: 100%; top: 392px; text-align: center; font-size: 21px; color: var(--ink); }
</style>
</head>
<body>
<main class="presentation">
  <div class="frame"></div>

  <section class="card card--front" aria-label="Business card front">
    <div class="front__topline"></div>

    <div class="brand">
      <span class="brand__dot"></span>
      <h1 class="brand__name">
        <span class="brand__line1">HARBOR POINT</span>
        <span class="brand__line2">MANAGEMENT</span>
      </h1>
    </div>

    <div class="person">
      <p class="person__name">Name Lastname</p>
      <p class="person__title">General Manager</p>
      <p class="person__cell">Cell:000-000-0000</p>
    </div>

    <address class="contact">
      <div class="contact__row contact__row--indent">123 Streetname</div>
      <div class="contact__row contact__row--indent">Bayside,ST 99999</div>
      <div class="contact__row">
        <svg class="contact__icon" viewBox="0 0 22 16" aria-label="Phone">
          <path d="M2 6 Q11 0 20 6 L18 8 L15 6 L15 4 Q11 2.5 7 4 L7 6 L4 8 Z" fill="var(--brand-blue)"/>
          <rect x="5" y="8" width="12" height="7" rx="1.5" fill="var(--brand-blue)"/>
        </svg>
        <span>000-000-0000</span>
        <span class="contact__gap"></span>
        <svg class="contact__icon" viewBox="0 0 22 16" aria-label="Fax">
          <rect x="1.5" y="3" width="19" height="10" rx="1" fill="none" stroke="var(--brand-blue)" stroke-width="1.5"/>
          <line x1="5" y1="7" x2="17" y2="7" stroke="var(--brand-blue)" stroke-width="1.2"/>
          <line x1="5" y1="9.5" x2="17" y2="9.5" stroke="var(--brand-blue)" stroke-width="1.2"/>
        </svg>
        <span>000-000-0000</span>
      </div>
      <div class="contact__row">
        <svg class="contact__icon" viewBox="0 0 22 16" aria-label="Email">
          <rect x="2" y="2" width="18" height="12" fill="none" stroke="var(--ink-soft)" stroke-width="1.3"/>
          <polyline points="2,2 11,9 20,2" fill="none" stroke="var(--ink-soft)" stroke-width="1.3"/>
        </svg>
        <span>name@harborpointmanagement.com</span>
      </div>
    </address>

    <svg class="front__bands" viewBox="0 0 770 42" aria-hidden="true">
      <polygon points="0,0 165,0 172,4 770,4 770,8 170,8 163,5 0,5" fill="var(--ink)"/>
      <polygon points="0,14 160,14 170,10 770,10 770,36 0,36" fill="var(--brand-blue)"/>
    </svg>
    <p class="front__web">www.harborpointmanagement.com</p>
  </section>

  <section class="card card--back" aria-label="Business card back">
    <div class="back__brand">
      <span class="back__dot"></span>
      <p class="back__name">HARBOR POINT MANAGEMENT</p>
    </div>
    <p class="back__web">www.harborpointmanagement.com</p>
  </section>
</main>
</body>
</html>
```